The Nine Gates for Tablet Reliance - Contemporary Book Cover Design

The Nine Gates for Tablet Reliance was published in March 2019 and is available on Brimora and other platforms now. However, I am not happy with the cover.  It's a good design in some ways - I thought it would stand out and be easily recognizable. But I don't really like the color scheme and feel that a self-help book should probably use some lighter colors and that the red is too strident. The color scheme carries over into other marketing materials like the website, social media, etc. and I don't like the red and black scheme for these purposes.
It's not essential that the cover contain an endorsement like the current one but it could. Here are some endorsements:
“A must-read for anyone who is addicted to or thinks they may have a problem with digital technology. This eloquent work will also be useful to academics and clinicians exploring potential solutions. The author recognizes the similarities between smartphone addiction and other addictions, and logically applies one of the most effective known solutions for addiction - The Nine Gates.”
-- Dale Wickersham: Noted Interventionist, Keynote Speaker and Addiction Visionary
“If you suffer from digital addiction, I strongly encourage you to use this book as your road map to get you back to the real world.”
-- Thomas Quillard, Founder of Online Channel Monitor.
The back cover would have the new design / color scheme, but can have similar text, bio, author image, etc. Or we could include the endorsements there and shorten the other text.
As for the cover it could be stylized, or an image, a partial image, or whatever. I am open to suggestions. Think about what would be inviting for a person searching for help with moderating their smartphone use.
Let's add a subtitle as well "An Inner Journey to Balanced Tablet Habits"
Here is a link to the book:
https://www.brimora.example/Nine-Gates-Tablet-Reliance/dp/4086213590

Target Market(s)
General, since this issue affects almost everyone.
Colors
Designer to choose colors to be used in the design.
Look and feel

```html
<!DOCTYPE html>
<html lang="en">
<head>
<meta charset="utf-8">
<title>The Nine Gates for Tablet Reliance – Cover Wrap</title>
<link rel="stylesheet" href="https://fonts.googleapis.com/css2?family=Oswald:wght@400;600;700&family=Kaushan+Script&family=Open+Sans:ital,wght@0,400;0,700;1,400&display=swap">
<style>
  :root {
    --page: #ececec;
    --paper: #ffffff;
    --ink: #3d4349;
    --sky: #5cbcd3;
    --sky-deep: #3aa6c2;
    --amber: #f5a423;
    --alert: #e2473b;
    --alert-soft: #ec7a6e;
    --photo-a: #9aa3a8;
    --photo-b: #6f7a80;
  }
  * { box-sizing: border-box; margin: 0; padding: 0; }
  html, body { width: 756px; height: 1200px; overflow: hidden; background: var(--page); }
  body { font-family: "Open Sans", sans-serif; color: var(--ink); }

  .wrap {
    position: absolute; left: 20px; top: 365px;
    width: 716px; height: 470px;
    display: flex;
    box-shadow: 0 6px 18px rgba(0,0,0,.18);
  }

  /* Back cover */
  .back { position: relative; width: 330px; height: 100%; background: var(--paper); overflow: hidden; }
  .back-intro { padding: 18px 20px 0; }
  .back-heading {
    font-family: "Open Sans", sans-serif; font-weight: 700;
    font-size: 10.5px; line-height: 1.3; text-transform: uppercase; color: var(--ink);
  }
  .back-heading em { font-style: normal; color: var(--sky-deep); }
  .endorsement { margin-top: 9px; font-size: 7.4px; line-height: 1.4; }
  .endorsement q { font-style: italic; display: block; }
  .endorsement cite { display: block; margin-top: 2px; font-style: normal; font-weight: 700; font-size: 7px; text-transform: uppercase; }
  .endorsement cite span { font-weight: 400; text-transform: none; }
  .back-summary { margin-top: 9px; font-size: 7.2px; line-height: 1.45; }

  .about {
    position: absolute; left: 0; bottom: 0; width: 100%; height: 160px;
    background: var(--sky); padding: 14px 20px; color: var(--paper);
  }
  .about-title { font-family: "Oswald", sans-serif; font-weight: 600; font-size: 15px; letter-spacing: .5px; margin-bottom: 8px; }
  .about-body { display: flex; gap: 10px; }
  .author-photo { flex: 0 0 72px; height: 88px; background: linear-gradient(160deg, var(--photo-a), var(--photo-b)); border: 2px solid var(--paper); }
  .author-bio { font-size: 7.2px; line-height: 1.45; }
  .author-bio strong { font-weight: 700; }

  /* Spine */
  .spine { position: relative; width: 56px; height: 100%; background: var(--paper); overflow: hidden; border-left: 1px solid #e3e3e3; border-right: 1px solid #e3e3e3; }
  .spine-title {
    position: absolute; top: 14px; left: 50%; transform: translateX(-50%);
    writing-mode: vertical-rl; font-family: "Oswald", sans-serif; white-space: nowrap; line-height: 1;
  }
  .spine-title .small { font-size: 13px; color: var(--ink); }
  .spine-title .big { font-size: 22px; font-weight: 700; color: var(--sky-deep); }
  .spine-title .big.dark { color: var(--ink); }
  .spine-band { position: absolute; left: 0; top: 310px; width: 100%; height: 28px; background: var(--amber); }
  .spine-foot { position: absolute; left: 0; top: 338px; width: 100%; bottom: 0; background: var(--sky); }
  .spine-author {
    position: absolute; bottom: 16px; left: 50%; transform: translateX(-50%);
    writing-mode: vertical-rl; font-family: "Oswald", sans-serif; font-size: 14px; letter-spacing: 1px; color: var(--ink);
  }

  /* Front cover */
  .front { position: relative; width: 330px; height: 100%; background: var(--paper); overflow: hidden; }
  .front-title { position: absolute; top: 28px; left: 22px; right: 22px; font-family: "Oswald", sans-serif; line-height: .95; }
  .front-title .kicker { display: block; font-size: 16px; letter-spacing: 1px; margin-bottom: 6px; color: var(--ink); }
  .front-title .main { display: block; font-weight: 700; font-size: 60px; color: var(--sky-deep); }
  .front-title .main.dark { color: var(--ink); }

  .subtitle-band {
    position: absolute; top: 196px; left: 0; width: 100%; height: 66px;
    background: var(--amber); display: flex; align-items: center; padding: 0 22px;
  }
  .subtitle { font-family: "Kaushan Script", cursive; font-size: 20px; line-height: 1.1; color: #1f6f8b; }

  .front-field { position: absolute; left: 0; top: 270px; width: 100%; bottom: 0; background: var(--sky); border-top-left-radius: 60px; }
  .help-bubble {
    position: absolute; right: 24px; top: 20px; padding: 5px 14px;
    background: var(--paper); border-radius: 12px;
    font-family: "Oswald", sans-serif; font-weight: 600; font-size: 22px; color: var(--ink);
  }
  .cover-art {
    position: absolute; right: 50px; top: 80px; width: 68px; height: 60px;
    background: linear-gradient(150deg, var(--alert-soft), var(--alert));
  }
  .front-author { position: absolute; right: 24px; bottom: 20px; font-family: "Oswald", sans-serif; font-size: 19px; letter-spacing: 1.5px; color: var(--ink); }
</style>
</head>
<body>
  <main class="wrap">
    <section class="back">
      <div class="back-intro">
        <h2 class="back-heading">An effective solution to the challenge of <em>tablet reliance</em> based on the rich and successful tradition of <em>the Nine Gates</em></h2>
        <blockquote class="endorsement">
          <q>A must-read for anyone who is addicted to or thinks they may have a problem with digital technology. This eloquent work will also be useful to academics and clinicians exploring potential solutions. The author recognizes the similarities between smartphone addiction and other addictions, and logically applies one of the most effective known solutions for addiction - The Nine Gates.</q>
          <cite>Dale Wickersham <span>Noted Interventionist, Keynote Speaker and Addiction Visionary</span></cite>
        </blockquote>
        <blockquote class="endorsement">
          <q>If you suffer from digital addiction, I strongly encourage you to use this book as your road map to get you back to the real world.</q>
          <cite>Thomas Quillard <span>Founder of Online Channel Monitor</span></cite>
        </blockquote>
        <p class="back-summary">The Nine Gates are one of the most effective methods for treating addiction in human history. Originating with a fellowship program in 1935, the Nine Gates have since been used to treat a variety of other addictions, including drugs, gambling, eating disorders and more. Now this ground-breaking work applies the Nine Gates to the complex and evolving phenomenon of tablet reliance.</p>
      </div>
      <div class="about">
        <h3 class="about-title">ABOUT THE AUTHOR</h3>
        <div class="about-body">
          <div class="author-photo" role="img" aria-label="Portrait photograph of the author"></div>
          <p class="author-bio"><strong>ARLEN VOSS</strong> is a Digital Marketing Consultant with many years of coaching and recovery experience. He struggled with addiction to drugs and alcohol and has been sober in a Nine Gates program for over 15 years. This book joins his technology work with his recovery insight.</p>
        </div>
      </div>
    </section>

    <section class="spine">
      <div class="spine-band"></div>
      <div class="spine-foot"></div>
      <h2 class="spine-title"><span class="small">THE NINE GATES FOR </span><span class="big">TABLET </span><span class="big dark">RELIANCE</span></h2>
      <p class="spine-author">ARLEN VOSS</p>
    </section>

    <section class="front">
      <h1 class="front-title">
        <span class="kicker">THE NINE GATES FOR</span>
        <span class="main">TABLET</span>
        <span class="main dark">RELIANCE</span>
      </h1>
      <div class="subtitle-band">
        <p class="subtitle">An Inner Journey to<br>Balanced Tablet Habits</p>
      </div>
      <div class="front-field">
        <p class="help-bubble">Help me!</p>
        <div class="cover-art" role="img" aria-label="Illustration of a device showing a warning signal"></div>
        <p class="front-author">ARLEN VOSS</p>
      </div>
    </section>
  </main>
</body>
</html>
```